Website Design for A Leading Live Casino Software Provider

We provide live casino software to other land based and online gaming establishments. We are a B2B provider.

```html
<!DOCTYPE html>
<html lang="en">
<head>
<meta charset="utf-8">
<title>Northlight Live Studios — Live Casino Software</title>
<link href="https://fonts.googleapis.com/css2?family=Open+Sans:wght@300;400;600;700&display=swap" rel="stylesheet">
<style>
:root{
  --brand-blue:#1d5597;
  --brand-blue-dark:#174479;
  --link-blue:#1f4f8c;
  --text:#333a40;
  --muted:#5a6168;
  --page-bg:#e9eaeb;
  --card-bg:#ffffff;
  --rule:#c9cdd1;
  --orange:#f6a623;
  --orange-dark:#e88f12;
  --dot-active:#f5a01d;
}
*{box-sizing:border-box;margin:0;padding:0}
html,body{width:1028px;height:1200px;overflow:hidden}
body{font-family:"Open Sans",Arial,sans-serif;color:var(--text);background:var(--page-bg);position:relative}
a{color:inherit;text-decoration:none}

.site-header{position:absolute;left:0;top:0;width:1028px;height:86px;background:linear-gradient(#fdfdfd,#eeeff0);border-bottom:1px solid #cfd2d5;box-shadow:0 2px 4px rgba(0,0,0,.08)}
.brand{position:absolute;left:100px;top:22px;display:flex;align-items:center;gap:10px;font-weight:700;font-size:30px;color:var(--brand-blue);letter-spacing:1px}
.brand-mark{width:26px;height:26px;border-radius:50%;background:var(--brand-blue)}
.brand-sub{position:absolute;left:100px;top:60px;font-size:9px;font-weight:700;letter-spacing:2.4px;color:var(--brand-blue-dark)}

.main-nav{position:absolute;left:396px;top:0;display:flex;height:86px}
.nav-item{width:90px;height:86px;border-left:1px solid #d4d7da;display:flex;flex-direction:column;align-items:center;padding-top:14px;font-size:12px;font-weight:600;color:#2b3035}
.nav-item:last-child{border-right:1px solid #d4d7da}
.nav-item.is-active{background:#fff;box-shadow:inset 0 -6px 0 var(--brand-blue)}
.nav-icon{width:40px;height:38px;border-radius:4px;margin-bottom:8px}
.icon-cards{background:linear-gradient(#f2f2f2,#b9423c)}
.icon-monitor{background:linear-gradient(#8e5bd0,#2d2f6a)}
.icon-paper{background:linear-gradient(#f4f4f4,#a7a7a7)}
.icon-reel{background:radial-gradient(circle,#6b6b6b,#1d1d1d)}
.icon-building{background:linear-gradient(#e0473d,#4a8ed8)}
.icon-mail{background:linear-gradient(#f3f7fb,#6fa3d6)}

.hero{position:absolute;left:102px;top:111px;width:822px;height:293px;background:linear-gradient(100deg,#1c4f8e 0%,#2b67ac 45%,#5a8fcb 100%);overflow:hidden;box-shadow:0 14px 18px -12px rgba(0,0,0,.45)}
.hero-photo{position:absolute;right:0;top:0;width:430px;height:293px;background:linear-gradient(180deg,#4a82c3 0%,#3a6fae 55%,#2f5a32 78%,#b53d33 100%)}
.hero-title{position:absolute;left:35px;top:44px;font-size:46px;font-weight:300;line-height:56px;color:#fff}
.hero-link{position:absolute;left:35px;top:171px;font-size:21px;font-weight:600;color:#fff}
.hero-dots{position:absolute;left:35px;top:247px;display:flex;gap:7px}
.hero-dots span{width:16px;height:16px;border-radius:50%;background:#fff}
.hero-dots span.is-active{background:var(--dot-active)}

.card{position:absolute;background:var(--card-bg);border:1px solid #d6d8db;box-shadow:0 1px 4px rgba(0,0,0,.12)}
.intro-card{left:103px;top:445px;width:538px;height:535px}
.intro-title{position:absolute;left:15px;top:16px;font-size:25px;font-weight:600;color:var(--brand-blue)}
.intro-body{position:absolute;left:15px;top:53px;width:500px;font-size:13.6px;line-height:17px;color:var(--text)}
.intro-body p{margin-bottom:17px}

.ribbon{position:absolute;height:40px;background:var(--brand-blue);color:#fff;display:flex;align-items:center}
.ribbon::after{content:"";position:absolute;right:-12px;top:0;border-style:solid;border-width:20px 0 20px 12px;border-color:transparent transparent transparent var(--brand-blue)}
.ribbon::before{content:"";position:absolute;left:0;bottom:-8px;border-style:solid;border-width:0 8px 8px 0;border-color:transparent #0f2f55 transparent transparent}
.products-ribbon{left:-9px;top:270px;width:520px;padding-left:24px;font-size:21px}
.dealers-ribbon{left:-9px;top:14px;width:246px;padding-left:18px;font-size:19px;font-weight:600}

.product{position:absolute;left:18px;width:502px;height:90px;border-bottom:1px solid var(--rule)}
.product-live{top:323px}
.product-kiosk{top:423px}
.product-thumb{position:absolute;left:0;top:0;width:118px;height:74px;border:1px solid #c5c8cb}
.thumb-table{background:linear-gradient(#4a4f58,#1f6b6a 60%,#0f4d4a)}
.thumb-kiosk{background:linear-gradient(90deg,#f3f3f3,#9ea3a8 50%,#f3f3f3)}
.product-name{position:absolute;left:136px;top:-2px;font-size:14px;font-weight:600;color:var(--brand-blue)}
.product-text{position:absolute;left:136px;top:16px;width:360px;font-size:13.6px;line-height:17px;color:var(--text)}
.more{font-size:11px;font-weight:700;color:var(--link-blue)}
.product .more{position:absolute;left:136px;top:55px}

.dealers-card{left:659px;top:445px;width:265px;height:311px}
.dealer-side{position:absolute;top:88px;width:56px;height:118px;opacity:.7}
.dealer-left{left:16px;background:linear-gradient(#d9a095,#8d3c3a)}
.dealer-right{right:13px;background:linear-gradient(#efe2d5,#c29a83)}
.dealer-main{position:absolute;left:74px;top:67px;width:120px;height:166px;background:#fff;border:1px solid #c9c9c9;box-shadow:0 2px 6px rgba(0,0,0,.35);padding:4px}
.dealer-photo{width:100%;height:100%;background:linear-gradient(#b4262a,#5b0e12 70%,#1a1a1a)}
.dealer-name{position:absolute;left:4px;bottom:4px;width:110px;background:rgba(0,0,0,.6);color:#fff;font-size:11px;font-weight:700;padding:3px 6px}
.dealers-caption{position:absolute;left:14px;top:248px;width:240px;font-size:11px;line-height:14px;color:var(--text)}
.dealers-card .more{position:absolute;left:14px;top:280px}

.news{position:absolute;left:659px;top:773px;width:265px}
.news-head{display:flex;align-items:center;gap:8px;padding-bottom:6px;border-bottom:1px solid var(--rule)}
.news-icon{width:32px;height:26px;background:linear-gradient(#f4f4f4,#a7a7a7);border-radius:2px}
.news-head h2{font-size:16.5px;font-weight:700;color:var(--brand-blue)}
.news-item{margin-top:9px;font-size:11px;line-height:14px;color:var(--muted)}
.news-item h3{font-size:11.5px;font-weight:700;color:var(--link-blue)}
.news-item .more{font-size:11px}

.cta-band{position:absolute;left:0;top:1008px;width:1028px;height:79px;background:linear-gradient(#3b70b4,#1e4f8e);border-top:1px solid #5a8ac5}
.cta-phone{position:absolute;left:103px;top:12px}
.cta-text{position:absolute;left:203px;top:14px;font-size:22.5px;line-height:26px;color:#fff;font-weight:400}
.cta-text strong{font-weight:700}
.cta-or{position:absolute;left:657px;top:24px;font-size:22px;color:#fff}
.cta-button{position:absolute;left:715px;top:21px;width:192px;height:41px;border-radius:5px;background:linear-gradient(var(--orange),var(--orange-dark));color:#fff;font-size:17px;font-weight:700;display:flex;align-items:center;justify-content:center;box-shadow:0 2px 3px rgba(0,0,0,.3)}

.site-footer{position:absolute;left:94px;top:1113px;width:680px;font-size:9px;font-weight:700;line-height:12px;color:#3a3f44}
.social{position:absolute;left:809px;top:1117px;display:flex;align-items:center;gap:10px;font-size:11px;font-weight:700;color:#3a3f44}
.social-dot{width:20px;height:20px;border-radius:50%;background:var(--brand-blue)}
</style>
</head>
<body>

<header class="site-header">
  <a class="brand" href="#"><span class="brand-mark"></span>NLS</a>
  <div class="brand-sub">NORTHLIGHT LIVE STUDIOS</div>
  <nav class="main-nav">
    <a class="nav-item is-active" href="#"><span class="nav-icon icon-cards" role="img" aria-label="Playing cards and chips icon"></span>Live Games</a>
    <a class="nav-item" href="#"><span class="nav-icon icon-monitor" role="img" aria-label="Desktop monitor icon"></span>Solutions</a>
    <a class="nav-item" href="#"><span class="nav-icon icon-paper" role="img" aria-label="Newspaper icon"></span>News/Events</a>
    <a class="nav-item" href="#"><span class="nav-icon icon-reel" role="img" aria-label="Film reel icon"></span>Videos</a>
    <a class="nav-item" href="#"><span class="nav-icon icon-building" role="img" aria-label="Casino building icon"></span>About</a>
    <a class="nav-item" href="#"><span class="nav-icon icon-mail" role="img" aria-label="Envelope icon"></span>Contact</a>
  </nav>
</header>

<section class="hero">
  <div class="hero-photo" role="img" aria-label="Business people in suits sprinting across a finish line on a running track under a blue sky"></div>
  <h1 class="hero-title">Always Ahead of<br>The Competition</h1>
  <a class="hero-link" href="#">Learn Why &#9656;</a>
  <div class="hero-dots"><span class="is-active"></span><span></span><span></span><span></span><span></span></div>
</section>

<main>
  <section class="card intro-card">
    <h2 class="intro-title">The Future of Internet Gaming is Here!</h2>
    <div class="intro-body">
      <p>We are Northlight Live Studios S.A. The preeminent providers of Live Interactive Streaming Games of Skill and Chance.</p>
      <p>The Online Gaming Industry has come a long way in the last decade. In today's very competitive market you must provide your customers with new and unique gaming venues. That's where we come in.</p>
      <p>Our suite of Live Interactive Games adds value to your existing gaming environments with no erosion of profit from your other established revenue sources. Our products are great Affiliate Drivers … LIve Interactive Gaming from NLS is your profit force multiplier!</p>
    </div>
    <div class="ribbon products-ribbon">Northlight Live Products</div>
    <article class="product product-live">
      <div class="product-thumb thumb-table" role="img" aria-label="Live dealer blackjack table streamed to players"></div>
      <h3 class="product-name">Live Dealer</h3>
      <p class="product-text">our beautiful and friendly dealers will interact securely with your customers.</p>
      <a class="more" href="#">Learn More &#9656;</a>
    </article>
    <article class="product product-kiosk">
      <div class="product-thumb thumb-kiosk" role="img" aria-label="Two free-standing gaming kiosk terminals"></div>
      <h3 class="product-name">TableLink Kiosk</h3>
      <p class="product-text">An innovative hardware implementation of all of our products for land based casinos and gaming outlets.</p>
      <a class="more" href="#">Learn More &#9656;</a>
    </article>
  </section>

  <aside class="card dealers-card">
    <div class="ribbon dealers-ribbon">Our Beautiful Dealers</div>
    <div class="dealer-side dealer-left" role="img" aria-label="Dealer portrait, partly hidden"></div>
    <div class="dealer-side dealer-right" role="img" aria-label="Dealer portrait, partly hidden"></div>
    <div class="dealer-main">
      <div class="dealer-photo" role="img" aria-label="Featured dealer holding playing cards in front of a red curtain"></div>
      <span class="dealer-name">+ Mara Quinn</span>
    </div>
    <p class="dealers-caption">They Will Ensure Your Players are Smiling Even when Losing!</p>
    <a class="more" href="#">Learn More &#9656;</a>
  </aside>

  <section class="news">
    <div class="news-head"><span class="news-icon" role="img" aria-label="Newspaper icon"></span><h2>Latest News and Events</h2></div>
    <div class="news-item"><h3>Lorem ipsum dolor sit amet</h3>Lorem ipsum dolor sit amet, consectetur adipi-scing elit... <a class="more" href="#">Learn More &#9656;</a></div>
    <div class="news-item"><h3>Lorem ipsum dolor sit amet</h3>Lorem ipsum dolor sit amet, consectetur adipi-scing elit... <a class="more" href="#">Learn More &#9656;</a></div>
    <div class="news-item"><h3>Lorem ipsum dolor sit amet</h3>Lorem ipsum dolor sit amet, consectetur adipi-scing elit... <a class="more" href="#">Learn More &#9656;</a></div>
  </section>
</main>

<section class="cta-band">
  <svg class="cta-phone" width="70" height="56" viewBox="0 0 70 56" aria-hidden="true">
    <path d="M8 20 Q35 2 62 20 L58 28 L48 24 L46 16 Q35 12 24 16 L22 24 L12 28 Z" fill="#f3a43a"/>
    <rect x="14" y="26" width="42" height="26" rx="5" fill="#dfe6ee" stroke="#8fa4bb" stroke-width="1.5"/>
    <g fill="#7a8ea6">
      <rect x="22" y="31" width="6" height="4" rx="1"/><rect x="32" y="31" width="6" height="4" rx="1"/><rect x="42" y="31" width="6" height="4" rx="1"/>
      <rect x="22" y="38" width="6" height="4" rx="1"/><rect x="32" y="38" width="6" height="4" rx="1"/><rect x="42" y="38" width="6" height="4" rx="1"/>
      <rect x="22" y="45" width="6" height="4" rx="1"/><rect x="32" y="45" width="6" height="4" rx="1"/><rect x="42" y="45" width="6" height="4" rx="1"/>
    </g>
  </svg>
  <p class="cta-text">Call Toll Free <strong>1-xxx-xxx-xxxx</strong> and get a<br><strong>FREE Demo</strong> of our Software and Solutions</p>
  <span class="cta-or">or</span>
  <a class="cta-button" href="#">Request Demo</a>
</section>

<footer class="site-footer">
  Northlight Live Studios is a leader among online casino software providers. Our team of expert internet casino software developers, managers and marketers are here to ensure that any project you need, is a project Northlight Live Studios can deliver. Our Casino services and consulting solutions can take your business to the next level. Our online casino software licensing can help any start up achieve the quickest and most secure return on investment.
</footer>
<div class="social">Get Social: <span class="social-dot"></span><span class="social-dot"></span></div>

</body>
</html>
```